The Molar Ledger (Cover Design for Ebook)

I need a cool and exciting eBook cover for my new book, launching very soon!
I want it to stand out and appeal to young professionals with big dreams.
It should be dramatic and bold and avoid cliche or generic photos. Simple design will work as long as it relates to the message of the book. The content will provide ten years of experience from working in the field and achieving success.
Title: The Molar Ledger (at the top)
(Subheading Updated) The secrets to money, motivation and success they don’t teach you in dental school
OR The secrets to success they don't teach you in dental school.
OR The secrets to money, motivation and success
(smaller under title)
Author Updated: Dr K Fenwick (place at the bottom)
Updates

Target Market(s)

Ambitious young dentists
See instagram www.snapverse.net/themolarledger for a sense of the style that I think could work.

Font styles to use
Serif
Sans Serif

Colors

Designer to choose colors to be used in the design.

Requirements
Must have
• Eye catching and cool.
• Show the benefits of success. Money, freedom, luxury
• Clear title and subheading
Nice to have
• Subtle dental reference
• dimensions 1600x2400
Should not have
• Boring photos of dentist/patients, dental clinic, teeth etc,

```html
<!DOCTYPE html>
<html lang="en">
<head>
<meta charset="utf-8">
<title>The Molar Ledger – Cover Options</title>
<link rel="stylesheet" href="https://fonts.googleapis.com/css2?family=Federo&family=Oranienbaum&family=Josefin+Sans:wght@600&display=swap">
<style>
  :root {
    --stage: #000000;
    --copper-light: #f3b27a;
    --copper: #d9783c;
    --copper-dark: #8a3a14;
    --band: rgba(170, 185, 200, 0.35);
    --frame-line: rgba(220, 230, 240, 0.35);
    --ink-light: #f2f2f2;
    --navy-top: #0c1e2e;
    --navy-mid: #3f6f94;
    --navy-low: #1d3d58;
    --steel-top: #2f4a62;
    --steel-mid: #9fb5cf;
    --steel-low: #557391;
    --char-top: #15171c;
    --char-mid: #2f323b;
    --char-low: #1d1f25;
    --taupe-top: #3e3634;
    --taupe-mid: #a49b95;
    --taupe-low: #5d5551;
  }
  * { margin: 0; padding: 0; box-sizing: border-box; }
  html, body { width: 869px; height: 1200px; overflow: hidden; background: var(--stage); }
  .sheet { position: relative; width: 869px; height: 1200px; }

  .cover {
    position: absolute; width: 422px; height: 592px;
    background: linear-gradient(135deg, var(--copper-light), var(--copper) 40%, var(--copper-dark));
  }
  .cover--navy  { left: 6px;   top: 4px; }
  .cover--steel { left: 440px; top: 4px; }
  .cover--char  { left: 6px;   top: 600px; }
  .cover--taupe { left: 440px; top: 600px; }

  .cover__face {
    position: absolute; inset: 0;
    border-radius: 46px;
    overflow: hidden;
  }
  .cover--navy  .cover__face { background: linear-gradient(180deg, var(--navy-top) 0%, var(--navy-low) 35%, var(--navy-mid) 52%, var(--navy-low) 75%, var(--navy-mid) 100%); }
  .cover--steel .cover__face { background: linear-gradient(180deg, var(--steel-top) 0%, var(--steel-low) 30%, var(--steel-mid) 50%, var(--steel-low) 78%, var(--steel-mid) 100%); }
  .cover--char  .cover__face { background: linear-gradient(180deg, var(--char-top) 0%, var(--char-low) 35%, var(--char-mid) 52%, var(--char-low) 100%); }
  .cover--taupe .cover__face { background: linear-gradient(180deg, var(--taupe-top) 0%, var(--taupe-low) 30%, var(--taupe-mid) 52%, var(--taupe-low) 80%, var(--taupe-mid) 100%); }

  .cover__rule {
    position: absolute; inset: 6px 8px;
    border: 1px solid var(--frame-line);
    border-radius: 42px;
  }

  .cover__title {
    position: absolute; left: 0; right: 0; top: 44px;
    text-align: center;
    font-family: "Federo", sans-serif;
    font-size: 58px; line-height: 88px;
    font-variant: small-caps;
    background: linear-gradient(180deg, var(--copper-light), var(--copper) 55%, var(--copper-dark));
    -webkit-background-clip: text; background-clip: text; color: transparent;
    filter: drop-shadow(2px 3px 2px rgba(0,0,0,0.55));
  }
  .cover__title--tall {
    top: 70px;
    font-family: "Oranienbaum", serif;
    font-variant: normal;
    font-size: 58px; line-height: 70px;
    transform: scaleY(1.55);
    letter-spacing: -1px;
  }

  .cover__emblem {
    position: absolute; left: 60px; top: 218px; width: 300px; height: 210px;
    border-radius: 40% 40% 50% 50%;
    background: radial-gradient(ellipse at 50% 50%, rgba(217,120,60,0.55), rgba(217,120,60,0.15) 55%, rgba(217,120,60,0) 72%);
  }

  .cover__band {
    position: absolute; left: 0; right: 0; top: 286px; height: 25px;
    background: linear-gradient(90deg, rgba(170,185,200,0.15), var(--band) 20%, var(--band) 80%, rgba(170,185,200,0.15));
    display: flex; align-items: center; justify-content: center;
    font-family: "Josefin Sans", sans-serif; font-weight: 600;
    font-size: 12.5px; letter-spacing: 0.6px;
    color: var(--ink-light);
    text-transform: uppercase;
  }

  .cover__author {
    position: absolute; left: 0; right: 0; top: 538px;
    text-align: center;
    font-family: "Josefin Sans", sans-serif; font-weight: 600;
    font-size: 21px; letter-spacing: 3px;
    color: var(--ink-light);
    text-transform: uppercase;
  }
</style>
</head>
<body>
<main class="sheet">
  <section class="cover cover--navy">
    <div class="cover__face">
      <div class="cover__rule"></div>
      <h1 class="cover__title">The Molar<br>Ledger</h1>
      <div class="cover__emblem" role="img" aria-label="Copper stylised tooth emblem"></div>
      <p class="cover__band">The secrets to money, motivation and success</p>
      <p class="cover__author">Kieran Fenwick</p>
    </div>
  </section>

  <section class="cover cover--steel">
    <div class="cover__face">
      <div class="cover__rule"></div>
      <h1 class="cover__title cover__title--tall">The Molar Ledger</h1>
      <div class="cover__emblem" role="img" aria-label="Copper stylised tooth emblem"></div>
      <p class="cover__band">The secrets to money, motivation and success</p>
      <p class="cover__author">Kieran Fenwick</p>
    </div>
  </section>

  <section class="cover cover--char">
    <div class="cover__face">
      <div class="cover__rule"></div>
      <h1 class="cover__title">The Molar<br>Ledger</h1>
      <div class="cover__emblem" role="img" aria-label="Copper stylised tooth emblem"></div>
      <p class="cover__band">The secrets to money, motivation and success</p>
      <p class="cover__author">Kieran Fenwick</p>
    </div>
  </section>

  <section class="cover cover--taupe">
    <div class="cover__face">
      <div class="cover__rule"></div>
      <h1 class="cover__title">The Molar<br>Ledger</h1>
      <div class="cover__emblem" role="img" aria-label="Copper stylised tooth emblem"></div>
      <p class="cover__band">The secrets to money, motivation and success</p>
      <p class="cover__author">Kieran Fenwick</p>
    </div>
  </section>
</main>
</body>
</html>
```